Corporate Design für Gebäudereinigung
Zielgruppe
Das Unternehmen ist in der Reinigungsbranche tätig. Es werden alle möglichen Reinigungstätigkeiten durchgeführt.
Von klassischer Unterhaltsreinigung in Stiegenhäusern oder Büros bis hin zu Spezialreinigungen wie Fassaden, Dächer, Denkmäler oder unterschiedlichsten Böden.
Zielgruppe kann kaum definiert werden, da Private wie auch Firmenkunden angesprochen werden sollen.
From classic maintenance cleaning in stairwells or offices to special cleaning such as facades, roofs, monuments or a wide variety of floors.
Target group can hardly be defined, since private as well as corporate customers should be addressed.
Aufgabenstellung
Wichtig ist, dass nicht zu viele Farben verwendet werden.
Design eher hell sprich 'sauber' nicht dunkel und schwerfällig.
Vielen Dank!
It is important not to use too many colors.
Design rather light, i.e. 'clean' not dark and impurely.
Thank you!

```html
<!DOCTYPE html>
<html lang="de">
<head>
<meta charset="utf-8">
<title>Glanzwerk Gebäudereinigung – Geschäftsausstattung</title>
<link href="https://fonts.googleapis.com/css2?family=Open+Sans:wght@600&family=Roboto:wght@400;500&display=swap" rel="stylesheet">
<style>
:root{
  --teal:#1cb5c4;
  --grey:#6d6e71;
  --ink:#111111;
  --paper:#ffffff;
  --bg:#ffffff;
  --shadow:rgba(0,0,0,.45);
}
*{box-sizing:border-box;margin:0;padding:0}
html,body{width:800px;height:1200px;overflow:hidden;background:var(--bg)}
body{position:relative;font-family:"Roboto",Arial,sans-serif;color:var(--ink);-webkit-font-smoothing:antialiased;-moz-osx-font-smoothing:grayscale}
.sheet{position:absolute;left:28px;top:26px;width:748px;height:1150px;background:var(--paper);box-shadow:4px 5px 6px var(--shadow)}
.wordmark{position:absolute;font-family:"Open Sans",Arial,sans-serif;font-weight:600;color:var(--grey);line-height:1;display:flex;align-items:center;gap:.35em;white-space:nowrap}
.wordmark .mark{width:.6em;height:.6em;background:currentColor;flex:none}
.wordmark .name{display:block}
.wordmark .name small{display:block;font-size:.45em;margin-top:.25em}
.hero-mark{left:0;width:100%;top:36px;justify-content:center;font-size:48px}
.letter{position:absolute;left:130px;top:195px;width:540px;height:760px;background:var(--paper);box-shadow:7px 7px 6px var(--shadow)}
.letter .wordmark{right:46px;top:50px;font-size:22px}
.sender{position:absolute;left:42px;top:94px;font-size:7.2px;line-height:9.6px}
.sender span{display:inline-block;width:18px}
.salutation{position:absolute;left:40px;top:185px;font-size:7.4px}
.body-copy{position:absolute;left:40px;top:201px;width:458px;font-size:7.15px;line-height:10.6px;text-align:justify;color:var(--ink)}
.body-copy p{margin-bottom:16px}
.closing{position:absolute;left:40px;top:568px;font-size:7.4px}
.signature{position:absolute;left:40px;top:582px;width:70px;height:36px;background:linear-gradient(90deg,#e6e6e6,#f5f5f5)}
.signer{position:absolute;left:42px;top:630px;font-size:8.6px;font-weight:500}
.role{position:absolute;left:42px;top:646px;font-size:7.2px}
.footer-address{position:absolute;left:0;width:100%;top:698px;text-align:center;font-size:7.4px}
.band{position:absolute;left:0;bottom:0;width:100%;height:18px}
.card{position:absolute;box-shadow:6px 6px 6px var(--shadow)}
.card-front{left:126px;top:998px;width:236px;height:146px;background:var(--paper)}
.card-front .wordmark{right:18px;top:16px;font-size:14px}
.card-front .holder{position:absolute;left:17px;top:72px;font-size:6.8px;font-weight:500}
.card-front .addr{position:absolute;left:17px;top:89px;font-size:6.2px;line-height:8px}
.card-front .contact{position:absolute;left:128px;top:89px;font-size:6.2px;line-height:8px}
.card-front .contact span{display:inline-block;width:16px}
.card-front .band{height:9px}
.card-back{left:437px;top:992px;width:234px;height:148px;background:var(--teal)}
.card-back .wordmark{left:0;width:100%;top:52px;justify-content:center;font-size:17px;color:#fff}
</style>
</head>
<body>
<div class="sheet">
  <div class="wordmark hero-mark"><span class="mark"></span><span class="name">GLANZWERK<small>Gebäudereinigung e.U.</small></span></div>
</div>

<section class="letter">
  <div class="wordmark"><span class="mark"></span><span class="name">GLANZWERK<small>Gebäudereinigung e.U.</small></span></div>
  <div class="sender">
    Glanzwerk Gebäudereinigung e.U.<br>
    <span>Fon</span>: 000.000.0000<br>
    <span>Fax</span>: 123.456.78910<br>
    <span>Mail</span>: xxx@glanzwerk.de<br>
    <span>Web</span>: www.glanzwerk.de
  </div>
  <div class="salutation">Sehr geehrte Damen und Herren</div>
  <div class="body-copy">
    <p>Lorem ipsum dolor sit amet, consectetur adipiscing elit. Fußball Nibh alle Lorem-Köcher-Effekte. Aber, und deshalb ist bibendum turpis ac, porttitor sehr wichtig. Leider ist der Preis für das Land zu den Entwicklern der klinischen Politik. Der Mauris ist es nun mal das Darlehen von einem nibh. Lorem fertigt jeden Preis. Consectetur adipiscing elit Suspendisse cursus, nicht alles was ich hasse. Jetzt fernsehfrei, innovativ absolviert. Jede Schokolade meine Tür und Ernährung. Donec sed velit ultricies risus vitae, ac pharetra nibh elementum. Ob Volleyball. Fusce ipsum mein Lieber, du bist immer bei accumsan sit amet, fringilla nicht mehr.</p>
    <p>Lorem ipsum dolor sit amet, consectetur adipiscing elit. Fußball Nibh alle Lorem-Köcher-Effekte. Aber, und deshalb ist bibendum turpis ac, porttitor sehr wichtig. Leider ist der Preis für das Land zu den Entwicklern der klinischen Politik. Der Mauris ist es nun mal das Darlehen von einem nibh. Lorem fertigt jeden Preis. Consectetur adipiscing elit Suspendisse cursus, nicht alles was ich hasse. Jetzt fernsehfrei, innovativ absolviert. Jede Schokolade meine Tür und Ernährung. Donec sed velit ultricies risus vitae, ac pharetra nibh elementum. Ob Volleyball. Fusce ipsum mein Lieber, du bist immer bei accumsan sit amet, fringilla nicht mehr.</p>
    <p>Lorem ipsum dolor sit amet, consectetur adipiscing elit. Fußball Nibh alle Lorem-Köcher-Effekte. Aber, und deshalb ist bibendum turpis ac, porttitor sehr wichtig. Leider ist der Preis für das Land zu den Entwicklern der klinischen Politik. Der Mauris ist es nun mal das Darlehen von einem nibh. Lorem fertigt jeden Preis. Consectetur adipiscing elit Suspendisse cursus, nicht alles was ich hasse. Jetzt fernsehfrei, innovativ absolviert. Jede Schokolade meine Tür und Ernährung. Donec sed velit ultricies risus vitae, ac pharetra nibh elementum. Ob Volleyball. Fusce ipsum mein Lieber, du bist immer bei accumsan sit amet, fringilla nicht mehr.</p>
    <p>Lorem ipsum dolor sit amet, consectetur adipiscing elit. Fußball Nibh alle Lorem-Köcher-Effekte. Aber, und deshalb ist bibendum turpis ac, porttitor sehr wichtig. Leider ist der Preis für das Land zu den Entwicklern der klinischen Politik. Der Mauris ist es nun mal das Darlehen von einem nibh. Lorem fertigt jeden Preis. Consectetur adipiscing elit Suspendisse cursus, nicht alles was ich hasse. Jetzt fernsehfrei, innovativ absolviert. Jede Schokolade meine Tür und Ernährung. Donec sed velit ultricies risus vitae, ac pharetra nibh elementum. Ob Volleyball. Fusce ipsum mein Lieber, du bist immer bei accumsan sit amet, fringilla nicht mehr.</p>
    <p>Lorem ipsum dolor sit amet, consectetur adipiscing elit. Fußball Nibh alle Lorem-Köcher-Effekte. Aber, und deshalb ist bibendum turpis ac, porttitor sehr wichtig. Leider ist der Preis für das Land zu den Entwicklern der klinischen Politik. Der Mauris ist es nun mal das Darlehen von einem nibh. Lorem fertigt jeden Preis. Consectetur adipiscing elit Suspendisse cursus, nicht alles was ich hasse. Jetzt fernsehfrei, innovativ absolviert. Jede Schokolade meine Tür und Ernährung. Donec sed velit ultricies risus vitae, ac pharetra nibh elementum. Ob Volleyball. Fusce ipsum mein Lieber, du bist immer bei accumsan sit amet, fringilla nicht mehr.</p>
  </div>
  <div class="closing">Mit freundlichen Grüßen,</div>
  <div class="signature" role="img" aria-label="Handschriftliche Unterschrift"></div>
  <div class="signer">jonaswagner</div>
  <div class="role">Direktor</div>
  <div class="footer-address">Lindenweg 12,&nbsp; Talheim, Rheinland-Pfalz(RP), 56400,&nbsp; 2604 11 22 33</div>
  <svg class="band" viewBox="0 0 540 18" preserveAspectRatio="none" aria-hidden="true">
    <polygon points="0,0 298,0 286,18 0,18" fill="var(--teal)"/>
    <polygon points="302,0 540,0 540,18 290,18" fill="var(--grey)"/>
  </svg>
</section>

<section class="card card-front">
  <div class="wordmark"><span class="mark"></span><span class="name">GLANZWERK<small>Gebäudereinigung e.U.</small></span></div>
  <div class="holder">jonaswagner, Direktor</div>
  <div class="addr">Lindenweg 12,<br>Talheim, Rheinland-Pfalz(RP)<br>56400,<br>2604 11 22 33</div>
  <div class="contact">
    <span>Fon</span>: 000.000.0000<br>
    <span>Fax</span>: 123.456.78910<br>
    <span>Mail</span>: xxx@glanzwerk.de<br>
    <span>Web</span>: www.glanzwerk.de
  </div>
  <svg class="band" viewBox="0 0 236 9" preserveAspectRatio="none" aria-hidden="true">
    <polygon points="0,0 124,0 118,9 0,9" fill="var(--teal)"/>
    <polygon points="127,0 236,0 236,9 121,9" fill="var(--grey)"/>
  </svg>
</section>

<section class="card card-back">
  <div class="wordmark"><span class="mark"></span><span class="name">GLANZWERK<small>Gebäudereinigung e.U.</small></span></div>
</section>
</body>
</html>
```